Flyer-Design für Sabine Wellrath Coaching für Führungskräfte
Zielgruppe
Coaching für Führungskräfte, Seminare für Führungskräfte.
Zielgruppe: Führungskräfte, Unternehmer, Geschäftsführer, Vorstände
Aufgabenstellung
Mein Logo soll beibehalten werden. Es soll ein vierseitiger Flyer sein, der meine Leistungen beschreibt. Es soll sehr modern sein (Stichwort: digital leadership) und seriös. Möglichst nicht das übliche Format, aber nicht zu groß.
Der Text soll weitgehend aus meiner Homepage (www.coaching-wellrath-beispiel.de) übernommen werden, aber es sollen auch zusätzlich Seminare aufgeführt werden.
Bis auf das Logo müssen die angehängten Dateien nicht unbedingt verwendet werden.

```html
<!DOCTYPE html>
<html lang="de">
<head>
<meta charset="utf-8">
<title>Flyer Sabine Wellrath Coaching</title>
<link rel="stylesheet" href="https://fonts.googleapis.com/css2?family=Source+Sans+3:wght@400;600;700&display=swap">
<style>
  :root {
    --backdrop: #808080;
    --paper: #ffffff;
    --ink: #1e1e24;
    --heading: #2f2f38;
    --accent: #3f5b86;
    --navy: #354a70;
    --band: #dde5ef;
    --brand: #1f5a8c;
    --fold: #e6e6e6;
  }
  * { margin: 0; padding: 0; box-sizing: border-box; }
  html, body { width: 1200px; height: 1200px; overflow: hidden; }
  body {
    background: var(--backdrop);
    font-family: "Source Sans 3", sans-serif;
    color: var(--ink);
    position: relative;
  }
  .spread {
    position: absolute; left: 15px; top: 184px;
    width: 1170px; height: 830px;
    background: var(--paper);
  }
  .page { position: absolute; top: 0; height: 830px; }
  .page--inside { left: 0; width: 585px; border-right: 1px solid var(--fold); }
  .page--cover { left: 585px; width: 585px; }

  .top-band { position: absolute; left: 20px; top: 0; width: 179px; height: 20px; background: var(--band); }
  .section-title {
    position: absolute; left: 20px; top: 78px;
    font-size: 22px; font-weight: 400; color: var(--heading); letter-spacing: .2px;
  }
  .col { position: absolute; top: 170px; width: 172px; font-size: 12.2px; line-height: 21px; }
  .col--one { left: 20px; }
  .col--two { left: 208px; top: 170px; }
  .col--three { left: 395px; width: 176px; }
  .col p + p, .col ul + p { margin-top: 21px; }
  .col ul { list-style: none; margin-top: 21px; }
  .col li { position: relative; padding-left: 12px; }
  .col li::before { content: "•"; position: absolute; left: 0; font-size: 10px; }
  .accent { color: var(--accent); font-weight: 600; }
  .contact { font-weight: 600; }

  .portrait {
    width: 171px; height: 139px; margin-bottom: 21px;
    background: linear-gradient(160deg, #d9d4cc 0%, #b9a58a 40%, #2b3352 75%, #cfcac2 100%);
  }
  .brand {
    position: absolute; left: 208px; top: 712px;
    display: flex; align-items: center; gap: 10px;
    color: var(--brand); font-weight: 600; font-size: 14px; line-height: 17px;
  }
  .brand-dot { width: 34px; height: 34px; border-radius: 50%; background: var(--brand); flex: none; }

  .cover-image {
    position: absolute; left: 35px; top: 20px; width: 546px; height: 790px;
    background: linear-gradient(180deg, #dfe6f3 0%, #eef2f8 22%, #f4f6fa 38%, #c9d3e5 52%, #8e9fc0 68%, #5a6d97 84%, #36466b 100%);
  }
  .cover-title {
    position: absolute; left: 56px; top: 65px; width: 417px; height: 168px;
    background: var(--paper); padding: 46px 0 0 33px;
    font-weight: 700; font-size: 35px; line-height: 47px; letter-spacing: 2.5px;
  }
  .cover-title .line-1 { color: var(--heading); display: block; }
  .cover-title .line-2 { color: var(--navy); display: block; }
</style>
</head>
<body>
  <div class="spread">
    <section class="page page--inside">
      <div class="top-band"></div>
      <h2 class="section-title">Meine Erfahrungen</h2>

      <div class="col col--one">
        <p>mehr als 20 Jahre in Führungs&shy;positionen in einem internatio&shy;nalen Unternehmen</p>
        <ul>
          <li>Personalauswahl, Coaching und Training</li>
          <li>Mediation (Mitglied im Fach&shy;verband Konfliktklärung)</li>
          <li>Psychotherapie (HPG)</li>
        </ul>
        <p class="accent">Es ist meine Berufung, Men&shy;schen in ihrem Arbeitsumfeld mit Wertschätzung auf dem Weg zu Zufriedenheit und Erfolg zu begleiten. Diese Begegnun&shy;gen haben mich reich an Erfah&shy;rung gemacht. Davon können Sie profitieren.</p>
      </div>

      <div class="col col--two">
        <div class="portrait" role="img" aria-label="Porträtfoto der Coachin im Gespräch"></div>
        <p>Coaching- und Mediationswei&shy;terbildung beim Netzwerk für Hochschulweiterbildung</p>
        <p>Univ. Zertifizierung als Media&shy;tor und Coach am Institut für Dialog und Vielfalt (IDV) an der Akademie für angewandte Psychologie und Führung (AAPF) Nordstadt www.aapf-beispiel.org/idv</p>
      </div>

      <div class="col col--three">
        <p>Wenn Sie mehr erfahren möch&shy;ten, empfehle ich ein Interview, welches durch www.leitwort-gespraeche.de mit mir geführt wurde.</p>
        <p class="accent">Bei Fragen oder Interesse an einer Beratung schreiben Sie mir per Mail oder rufen Sie mich direkt an unter 0160 48127739. Gerne können wir Termine vereinbaren, ich freue mich auf Sie!</p>
        <p class="contact">Sabine Wellrath<br>Coaching für Führungskräfte<br>Am Lindenbogen 8<br>47829 Talheim</p>
        <p class="contact">Mobil: 0160 48127739<br>E-Mail:<br><span style="font-size:11px">anfrage57@coaching-wellrath-beispiel.de</span></p>
      </div>

      <div class="brand">
        <span class="brand-dot"></span>
        <span>Sabine Wellrath<br>Coaching für Führungskräfte</span>
      </div>
    </section>

    <section class="page page--cover">
      <div class="cover-image" role="img" aria-label="Schneebedeckter Berggipfel unter hellem, bewölktem Himmel"></div>
      <h1 class="cover-title">
        <span class="line-1">COACHING</span>
        <span class="line-2">SABINE WELLRATH</span>
      </h1>
    </section>
  </div>
</body>
</html>
```